business card with 2 locations on 1 card

I need a modern looking business card that I would use at 2 different locations. Possibly 1 location on 1 side and other location on other side. One should be able to distinguish the 2 locations immediately before having to read the address or description on card. You can take a look at my website to see what I'm drawn to. The logo is brand new that I just purchased on Craft Hive. I want to emphasize family.
Updates

Let's not use the yellow and blue colors. Added Thursday, August 31, 2017

Target Market(s)

women and children

Industry/Entity Type

Health And Wellness

Contact Information for Business Card

Business name: Willow Brook Chiropractic & Acupuncture
My name: Lorin Daske
Job title: DC, MSOM, LAc (NM), CNC

Location 1
Address: 4817 Marlowe Blvd, Suite C-210, Larkmoor, TX 75390
Phone: (469) 555-0182
Fax: (972) 555-0137

Location 2
Address: 1936 Belvane Road, Suite 300, Pinecrest, TX 75312
Phone: (469) 555-0169
Fax: (972) 555-0137

Email: drlorindaske@mailnest.example
Website: www.drlorindaske.example

Font styles to use
Serif
Sans Serif

Colors

Designer to choose colors to be used in the design.

Requirements
Must have
• distinction between 2 locations.
Nice to have
• Colors preference below is there. But I like to see what you come up with too!

```html
<!DOCTYPE html>
<html lang="en">
<head>
<meta charset="utf-8">
<title>Willow Brook Chiropractic &amp; Acupuncture – Business Card</title>
<link rel="stylesheet" href="https://fonts.googleapis.com/css2?family=Montserrat:wght@400;500;700&display=swap">
<style>
  :root {
    --teal: #277a6b;
    --green: #21b20a;
    --paper: #ffffff;
    --ink-light: #ffffff;
  }
  * { margin: 0; padding: 0; box-sizing: border-box; }
  html, body { width: 1200px; height: 804px; overflow: hidden; background: var(--paper); }
  .card {
    position: relative;
    width: 1200px;
    height: 804px;
    background: var(--paper);
    font-family: "Montserrat", sans-serif;
    color: var(--teal);
  }
  .brand-mark {
    position: absolute;
    left: 79px; top: 81px;
    width: 250px; height: 250px;
  }
  .brand-mark svg { display: block; }
  .business-name {
    position: absolute;
    left: 360px; top: 147px;
    font-size: 24px; font-weight: 700;
    letter-spacing: 5.5px;
    white-space: nowrap;
  }
  .person-name {
    position: absolute;
    left: 360px; top: 240px;
    font-size: 36px; font-weight: 700;
    letter-spacing: 6px;
  }
  .credentials {
    position: absolute;
    left: 360px; top: 292px;
    font-size: 35px; font-weight: 400;
    letter-spacing: 6.5px;
    white-space: nowrap;
  }
  .locations {
    position: absolute;
    left: 0; top: 365px;
    width: 1200px; height: 258px;
    display: flex;
  }
  .location {
    height: 100%;
    color: var(--ink-light);
    font-size: 28px; font-weight: 400;
    letter-spacing: 6px;
    line-height: 33px;
    padding-top: 31px;
    white-space: nowrap;
  }
  .location--larkmoor { width: 600px; background: var(--teal); padding-left: 77px; }
  .location--pinecrest { width: 600px; background: var(--green); padding-left: 71px; }
  .location-contact { margin-top: 33px; }
  .web-contact {
    position: absolute;
    left: 0; top: 646px;
    width: 1193px;
    text-align: center;
    font-size: 24px; font-weight: 500;
    letter-spacing: 2.5px;
    line-height: 42px;
  }
</style>
</head>
<body>
  <main class="card">
    <div class="brand-mark">
      <svg width="250" height="250" viewBox="0 0 250 250" role="img" aria-label="Willow Brook brand mark">
        <circle cx="125" cy="125" r="119" fill="none" stroke="var(--teal)" stroke-width="10"/>
        <text x="125" y="133" text-anchor="middle" font-family="Montserrat, sans-serif" font-size="24" font-weight="700" letter-spacing="2" fill="var(--teal)">Willow Brook</text>
      </svg>
    </div>

    <p class="business-name">Willow Brook Chiropractic &amp; Acupuncture</p>
    <h1 class="person-name">Lorin Daske</h1>
    <p class="credentials">DC, MSOM, LAc (NM), CNC</p>

    <section class="locations">
      <div class="location location--larkmoor">
        <p class="location-address">Address: 4817 Marlowe<br>Blvd, Suite C-210,<br>Larkmoor, TX 75390</p>
        <p class="location-contact">Phone: (469) 555-0182<br>Fax: (972) 555-0137</p>
      </div>
      <div class="location location--pinecrest">
        <p class="location-address">Address: 1936 Belvane<br>Road, Suite 300,<br>Pinecrest, TX 75312</p>
        <p class="location-contact">Phone: (469) 555-0169<br>Fax: (972) 555-0137</p>
      </div>
    </section>

    <div class="web-contact">
      <p>Email: drlorindaske@mailnest.example</p>
      <p>Website: www.drlorindaske.example</p>
    </div>
  </main>
</body>
</html>
```